Residential Construction Business - Site Signage

I need a design made for a site fence banner. We have a logo and branding so the design would need to be aligned with this. It would need to be made to specific size ratio so that it can be sent to the maker for production.
ratio : 4600 wide x 1700 high
The design should feature our website and also the slogan
"STAY PUT, BUILD BETTER"

Target Market(s)

potential clients

Industry/Entity Type

construction

Font styles to use
Other font styles liked:
• to match branding

Colors
0054AA
0677BA
7BADD7
CADEEF
E8F1F8

Requirements
Must have
• www.velmbuild.com.au Majority of the sign is our brand logo
Nice to have
• Majority of the sign is our brand logo
Should not have
• colors and themes that arent brand relevant

```html
<!DOCTYPE html>
<html lang="en">
<head>
<meta charset="utf-8">
<title>Velmbuild – Site Fence Banner</title>
<link rel="stylesheet" href="https://fonts.googleapis.com/css2?family=Montserrat:wght@400;500;600;700&display=swap">
<style>
  :root {
    --backdrop: #bfbfbf;
    --brand-navy: #053b5c;
    --banner-white: #ffffff;
  }
  html, body {
    margin: 0;
    padding: 0;
    width: 1200px;
    height: 1200px;
    overflow: hidden;
    background: var(--backdrop);
  }
  .stage {
    position: relative;
    width: 1200px;
    height: 1200px;
  }
  .fence-banner {
    position: absolute;
    left: 97px;
    top: 412px;
    width: 1006px;
    height: 376px;
    box-shadow: 0 4px 18px rgba(0, 0, 0, 0.45);
    background: var(--banner-white);
  }
  .fence-banner svg {
    display: block;
  }
  .chevron-panel { fill: var(--brand-navy); }
  .brand-name {
    font-family: "Montserrat", sans-serif;
    font-weight: 600;
    font-size: 54px;
    fill: var(--brand-navy);
  }
  .tagline {
    font-family: "Montserrat", sans-serif;
    font-weight: 500;
    font-size: 22px;
    letter-spacing: 3px;
    fill: var(--brand-navy);
  }
  .web-address {
    font-family: "Montserrat", sans-serif;
    font-weight: 500;
    font-size: 15px;
    fill: var(--brand-navy);
  }
  .web-address .domain-strong { font-weight: 700; }
</style>
</head>
<body>
  <main class="stage">
    <section class="fence-banner" aria-label="Velmbuild site fence banner">
      <svg width="1006" height="376" viewBox="0 0 1006 376" xmlns="http://www.w3.org/2000/svg">
        <path class="chevron-panel"
              d="M0 0 H396 L248 160 Q230 186 250 214 L409 376 H0 Z"/>

        <text class="brand-name" x="262" y="207" textLength="454" lengthAdjust="spacing">VELMBUILD</text>

        <text class="tagline" x="767" y="185">STAY PUT,</text>
        <text class="tagline" x="767" y="227">BUILD BETTER</text>

        <text class="web-address" x="766" y="317" textLength="214" lengthAdjust="spacingAndGlyphs">www.<tspan class="domain-strong">velmbuild</tspan>.com.au</text>
      </svg>
    </section>
  </main>
</body>
</html>
```